サイト構成・基本的な要件については
https://drawlumo.com/boards/R3TX9pamqzeh2WnL
を併せてご覧いただければ幸いです。
※導線が確保されていれば、必ずしもレイアウト案に忠実である必要はございません。
ぜひご提案いただければ幸甚です。

また、素材については
http://parcelvault.jp/get/91a7c2e05d4f18b6a3c29e7d10f5b84a2e6c90d3
よりダウンロードいただければと存じます。

上記だけで制作が難しい場合は
http://fotomoru.jp/
などから、5000円程度までならこちらにて購入可能です。カンプデータにて作成頂き、
納品時に当方にて購入したデータに差し替えていただければと存じます。

全体的なデザインのイメージとしては

http://www.plumrow-garden.jp/
http://www.tavolix.co.jp/bitemode/
http://verdalio.jp/
http://yu-morikawa.com/
のような、白ベースですっきりと見やすい印象が希望です。

メインカラーは既存サイトと同様、グリーンでお願いします。
http://www.sakuradaplate.co.jp/
1ページ
白を基調とし、グリーンベースでスッキリと明るく見やすいデザインを希望します
素材については
よりダウンロードいただければと存じます。

上記だけで制作が難しい場合は
http://fotomoru.jp/

白ベースでメインカラーは既存と同様にグリーンを使用し、
明るく見やすいデザインをお願いできればと思います。

http://baseline-gallery.com/2012/208.html
http://baseline-gallery.com/2011/143.html
→フッター部分の参照

基本レイアウト
については、必ずしも忠実である必要はありません。

是非ご提案お待ちしております。
何卒よろしくお願いいたします。

制作につきましてご不明な点がございましたら、お気軽にお申し付けいただければと存じます。
ご提案お待ちしております。

クライアント様との協議の結果こちらの案を採用させていただきました。
高級感と柔らかさのバランスがとてもよく、
視認性も高く、要望を全て満たしておりましたので
こちらの案を採用いたしました。

この度は多数ご提案いただきありがとうございました。
当選に至らなかったランサー様におかれましては大変心苦しいのですが、
またの機会にぜひご提案いただければ幸甚です。
引き続き何卒よろしくお願いいたします。

```html
<!DOCTYPE html>
<html lang="ja">
<head>
<meta charset="utf-8">
<title>桜田クッキング</title>
<link rel="stylesheet" href="https://fonts.googleapis.com/css2?family=Noto+Sans+JP:wght@400;500;700&family=Lato:wght@400;700&display=swap">
<style>
:root{
  --green:#6cb52d;
  --green-dark:#4f9a1a;
  --green-light:#e9f4dc;
  --yellow:#f7ea3c;
  --text:#444;
  --muted:#888;
  --line:#dcdcdc;
  --bg-soft:#f4f4f2;
}
*{box-sizing:border-box;margin:0;padding:0}
html,body{width:1200px;height:2624px;overflow:hidden}
body{background:#fff;color:var(--text);font-family:"Noto Sans JP",sans-serif;font-size:13px;line-height:1.5;position:relative}
ul{list-style:none}
.wrap{width:960px;margin:0 auto;position:relative}

/* header */
.site-header{height:150px;display:flex;flex-direction:column;align-items:center;justify-content:center}
.brand{display:flex;align-items:center;gap:14px}
.brand-mark{width:40px;height:40px;border-radius:50%;background:var(--green)}
.brand-name{font-size:30px;font-weight:500;color:var(--text);letter-spacing:2px;line-height:1.1}
.brand-sub{font-family:"Lato",sans-serif;font-size:12px;color:var(--muted);letter-spacing:3px;margin-top:4px}

.global-nav{border-top:3px solid var(--green);border-bottom:3px solid var(--green);height:48px;margin-top:10px}
.global-nav ul{display:flex;height:100%}
.global-nav li{flex:1;display:flex;align-items:center;justify-content:center;gap:6px;font-size:13px;border-left:1px solid var(--line)}
.global-nav li:last-child{border-right:1px solid var(--line)}
.global-nav li.is-current{background:var(--yellow)}
.global-nav svg{width:14px;height:14px}

/* hero */
.hero{background:var(--bg-soft);margin-top:40px;padding:0;height:392px}
.hero .wrap{display:grid;grid-template-columns:300px 220px 220px 220px;height:392px}
.hero-lead{position:relative;background:linear-gradient(160deg,#f1efe8,#e3ddcf)}
.hero-lead .copy{position:absolute;left:24px;top:80px;width:250px;background:rgba(255,255,255,.85);padding:16px}
.hero-lead h1{color:var(--green);font-size:24px;font-weight:700;line-height:1.3}
.hero-lead p{font-size:11px;color:var(--text);margin-top:8px}
.ph{display:block}
.ph-a{background:linear-gradient(180deg,#e6e2d8,#c9b9a0)}
.ph-stack{display:grid;grid-template-rows:1fr 1fr}
.ph-b{background:linear-gradient(135deg,#eae6dc,#d8cbb3)}
.ph-c{background:linear-gradient(135deg,#d9634a,#a9c56b)}
.ph-d{background:linear-gradient(180deg,#f0eee9,#c8cfc0)}

/* contact band */
.contact{padding:18px 0}
.contact-bar{width:760px;margin:0 auto;height:40px;border-radius:20px;background:var(--yellow);display:flex;align-items:center;justify-content:center;gap:10px;font-size:17px;font-weight:700;color:var(--green-dark)}
.contact-bar svg{width:22px;height:22px}
.contact-phones{display:flex;justify-content:center;gap:30px;margin-top:12px}
.phone{display:flex;align-items:center;gap:10px}
.phone .school{background:var(--green);color:#fff;font-size:11px;padding:2px 10px;border-radius:2px}
.phone .num{font-family:"Lato",sans-serif;font-size:20px;font-weight:700;color:var(--green-dark);letter-spacing:1px}

/* news */
.news{display:grid;grid-template-columns:1fr 1fr;gap:20px;margin-top:20px;height:360px}
.block-title{display:flex;align-items:center;gap:8px;font-size:17px;font-weight:700;color:var(--green-dark);border-bottom:3px solid var(--green);padding-bottom:6px}
.block-title::before{content:"";width:26px;height:26px;border-radius:3px;background:var(--green-light);border:2px solid var(--green)}
.news-list li{border-bottom:1px dotted var(--line);padding:8px 4px}
.news-list time{display:block;font-size:11px;color:var(--muted)}
.news-list span{font-size:12px;color:var(--green-dark)}

/* main area */
.main-area{display:grid;grid-template-columns:200px 730px;gap:30px;margin-top:20px;height:980px}
.side-contact{background:var(--green);padding:16px 14px;color:#fff;border-radius:3px}
.side-contact .tag{background:var(--yellow);color:var(--green-dark);font-weight:700;font-size:13px;text-align:center;padding:4px;border-radius:2px}
.side-contact dl{margin-top:8px}
.side-contact dt{font-size:11px;margin-top:8px}
.side-contact dd{font-family:"Lato",sans-serif;font-size:22px;font-weight:700;line-height:1.2}
.side-contact .note{font-size:10px;margin-top:10px;text-align:center}
.side-nav{margin-top:20px;border-top:1px solid var(--line)}
.side-nav li{border-bottom:1px solid var(--line);padding:7px 12px;font-size:12px;display:flex;align-items:center;gap:8px}
.side-nav li::before{content:"";width:5px;height:5px;border-top:2px solid var(--green);border-right:2px solid var(--green);transform:rotate(45deg)}
.side-banner{margin-top:14px;height:70px;border:1px solid var(--line);display:flex;align-items:center;gap:12px;padding:0 12px;font-size:13px;font-weight:700;color:var(--green-dark)}
.side-banner .icon{width:44px;height:44px;border-radius:50%;background:var(--green-light)}

.section-title{display:flex;align-items:center;gap:10px;font-size:19px;font-weight:700;color:var(--green-dark);border-bottom:3px solid var(--green);padding-bottom:8px}
.section-title .thumb{width:40px;height:34px;background:linear-gradient(135deg,#e0873a,#b54a2c)}
.courses{display:grid;grid-template-columns:1fr 1fr;gap:26px 30px;margin-top:22px}
.course .photo{height:160px}
.course h3{font-size:15px;color:var(--green-dark);font-weight:700;margin-top:8px;padding-left:10px;border-left:4px solid var(--green)}
.course p{font-size:11px;color:var(--muted);margin-top:4px}
.p1{background:linear-gradient(135deg,#f3efe6,#c9b79a)}
.p2{background:linear-gradient(135deg,#a4471f,#d98c3c)}
.p3{background:linear-gradient(135deg,#d9d3c8,#9b7a5c)}
.p4{background:linear-gradient(135deg,#eef1f3,#b8c6d2)}
.p5{background:linear-gradient(135deg,#9ed35a,#3f8f1f)}
.p6{background:linear-gradient(135deg,#f1f1f1,#c9c9c9)}

.page-top{text-align:right;font-family:"Lato",sans-serif;font-size:11px;color:var(--green-dark);margin-top:10px;display:flex;justify-content:flex-end;align-items:center;gap:6px}
.page-top i{width:14px;height:14px;border-radius:50%;background:var(--green)}

/* footer */
.footer-band{background:var(--green);margin-top:20px;padding:30px 0}
.footer-band .inner{background:#fff;width:960px;margin:0 auto;padding:22px 0;border-radius:4px}
.footer-nav{margin-top:12px}
.footer-bottom{display:flex;justify-content:space-between;margin-top:18px;font-size:10px;color:var(--muted)}
.footer-links{display:flex;gap:14px}
.footer-info{text-align:right;line-height:1.7}
</style>
</head>
<body>

<header class="site-header">
  <div class="brand">
    <span class="brand-mark"></span>
    <div>
      <div class="brand-name">桜田クッキング</div>
      <div class="brand-sub">Sakurada cooking school</div>
    </div>
  </div>
</header>
<nav class="global-nav wrap" style="margin-top:10px">
  <ul>
    <li><svg viewBox="0 0 14 14"><path d="M1 7 7 1l6 6M3 6v7h8V6" fill="none" stroke="#6cb52d" stroke-width="1.6"/></svg>桜田クッキングについて</li>
    <li>入会案内</li>
    <li>コース案内</li>
    <li>料金表</li>
    <li class="is-current">よくある質問</li>
    <li>教室案内</li>
  </ul>
</nav>

<section class="hero">
  <div class="wrap">
    <div class="hero-lead" role="img" aria-label="料理教室で野菜を調理する様子の写真">
      <div class="copy">
        <h1>実習こそが上達への近道</h1>
        <p>一人ひとりの習熟度に合わせ、基礎から丁寧に指導いたします。楽しく学べる教室です。</p>
      </div>
    </div>
    <span class="ph ph-a" role="img" aria-label="調理台で料理をする講師の写真"></span>
    <div class="ph-stack">
      <span class="ph ph-b" role="img" aria-label="包丁と食材の写真"></span>
      <span class="ph ph-c" role="img" aria-label="色とりどりの野菜の写真"></span>
    </div>
    <span class="ph ph-d" role="img" aria-label="完成した料理を持つシェフの写真"></span>
  </div>
</section>

<section class="contact">
  <div class="contact-bar">
    <svg viewBox="0 0 24 24"><path d="M6.6 10.8a15 15 0 0 0 6.6 6.6l2.2-2.2a1 1 0 0 1 1-.25 11 11 0 0 0 3.6.57 1 1 0 0 1 1 1V20a1 1 0 0 1-1 1A17 17 0 0 1 3 4a1 1 0 0 1 1-1h3.5a1 1 0 0 1 1 1c0 1.25.2 2.45.57 3.57a1 1 0 0 1-.25 1z" fill="#4f9a1a"/></svg>
    体験レッスン・見学受付中！お問い合わせはこちら
  </div>
  <div class="contact-phones">
    <div class="phone"><span class="school">有楽町校</span><span class="num">03-4180-2217</span></div>
    <div class="phone"><span class="school">日本橋校</span><span class="num">03-4192-0583</span></div>
    <div class="phone"><span class="school">柏校</span><span class="num">04-7290-3146</span></div>
  </div>
</section>

<section class="news wrap">
  <div>
    <h2 class="block-title">新着情報</h2>
    <ul class="news-list">
      <li><time>2014年12月25日</time><span>年末年始の休講日についてのお知らせ</span></li>
      <li><time>2014年12月20日</time><span>新春特別レッスンの受付を開始しました</span></li>
      <li><time>2014年12月15日</time><span>日本橋校の教室案内ページを更新しました</span></li>
      <li><time>2014年12月10日</time><span>短期集中コースの日程を追加しました</span></li>
      <li><time>2014年12月05日</time><span>体験レッスンの空き状況をお知らせします</span></li>
    </ul>
  </div>
  <div>
    <h2 class="block-title">今月のメニュー紹介</h2>
    <ul class="news-list">
      <li><time>2014年12月25日</time><span>冬野菜のポタージュと焼きたてパン</span></li>
      <li><time>2014年12月20日</time><span>鶏肉の赤ワイン煮込みと彩りサラダ</span></li>
      <li><time>2014年12月15日</time><span>季節の魚を使った和食の基本献立</span></li>
      <li><time>2014年12月10日</time><span>クリスマス向けのローストチキン</span></li>
      <li><time>2014年12月05日</time><span>手作りおせちの基本とお雑煮</span></li>
    </ul>
  </div>
</section>

<section class="main-area wrap">
  <aside>
    <div class="side-contact">
      <div class="tag">体験レッスン・見学受付中</div>
      <dl>
        <dt>有楽町校</dt><dd>03-4180-2217</dd>
        <dt>日本橋校</dt><dd>03-4192-0583</dd>
        <dt>柏校</dt><dd>04-7290-3146</dd>
      </dl>
      <p class="note">お気軽にお問い合わせください</p>
    </div>
    <ul class="side-nav">
      <li>ホーム</li>
      <li>桜田クッキングについて</li>
      <li>入会案内</li>
      <li>コース案内</li>
      <li>料金表</li>
      <li>よくある質問</li>
      <li>教室案内</li>
    </ul>
    <div class="side-banner"><span class="icon"></span>出張の指導へ</div>
    <div class="side-banner"><span class="icon"></span>体験レッスン</div>
  </aside>

  <div>
    <h2 class="section-title"><span class="thumb" role="img" aria-label="料理の写真"></span>桜田クッキングについて</h2>
    <div class="courses">
      <article class="course"><div class="photo p1" role="img" aria-label="教室で調理する生徒の写真"></div><h3>桜田クッキングの特徴</h3><p>少人数制で一人ひとりに合わせた丁寧な指導を行っています。</p></article>
      <article class="course"><div class="photo p2" role="img" aria-label="煮込み料理の写真"></div><h3>レギュラーコース</h3><p>基礎から応用まで、毎月の献立で幅広く学べるコースです。</p></article>
      <article class="course"><div class="photo p3" role="img" aria-label="鍋と調理器具の写真"></div><h3>専門・特別コース</h3><p>和洋中の専門的な技術を本格的に身につけるコースです。</p></article>
      <article class="course"><div class="photo p4" role="img" aria-label="講師が指導する様子の写真"></div><h3>短期集中コース</h3><p>短い期間で効率よく料理の基本を習得できるコースです。</p></article>
      <article class="course"><div class="photo p5" role="img" aria-label="新緑の木々の写真"></div><h3>サンデーコース</h3><p>お仕事帰りや休日にも通いやすい日曜日のコースです。</p></article>
      <article class="course"><div class="photo p6" role="img" aria-label="エプロン姿の人々の写真"></div><h3>男性コース</h3><p>男性のための料理入門。包丁の持ち方から学べます。</p></article>
    </div>
  </div>
</section>

<div class="wrap page-top"><i></i>PAGE TOP</div>

<footer>
  <div class="footer-band">
    <div class="inner">
      <div class="contact-bar">
        <svg viewBox="0 0 24 24"><path d="M6.6 10.8a15 15 0 0 0 6.6 6.6l2.2-2.2a1 1 0 0 1 1-.25 11 11 0 0 0 3.6.57 1 1 0 0 1 1 1V20a1 1 0 0 1-1 1A17 17 0 0 1 3 4a1 1 0 0 1 1-1h3.5a1 1 0 0 1 1 1c0 1.25.2 2.45.57 3.57a1 1 0 0 1-.25 1z" fill="#4f9a1a"/></svg>
        体験レッスン・見学受付中！お問い合わせはこちら
      </div>
      <div class="contact-phones">
        <div class="phone"><span class="school">有楽町校</span><span class="num">03-4180-2217</span></div>
        <div class="phone"><span class="school">日本橋校</span><span class="num">03-4192-0583</span></div>
        <div class="phone"><span class="school">柏校</span><span class="num">04-7290-3146</span></div>
      </div>
    </div>
  </div>
  <nav class="global-nav footer-nav wrap">
    <ul>
      <li><svg viewBox="0 0 14 14"><path d="M1 7 7 1l6 6M3 6v7h8V6" fill="none" stroke="#6cb52d" stroke-width="1.6"/></svg>桜田クッキングについて</li>
      <li>入会案内</li>
      <li>コース案内</li>
      <li class="is-current">料金表</li>
      <li>よくある質問</li>
      <li>教室案内</li>
    </ul>
  </nav>
  <div class="wrap footer-bottom">
    <ul class="footer-links"><li>プライバシーポリシー</li><li>｜ サイトマップ</li><li>｜ お問い合わせ</li></ul>
    <div class="footer-info">桜田クッキング 東京都千代田区有楽町 0-0-0 桜田ビル 2F<br>Copyright © 2014 Sakurada Cooking. All Rights Reserved.</div>
  </div>
</footer>

</body>
</html>
```